Classy business card for accounting firm

We're looking for a new business card for our accounting firm. Our logo was designed by Brandolith, so all of the design info we would like to use has been provided. The specific font provided isn't required to be used.

We want the card to look classy and elegent. Probably more minimalistic, but still with some pops of color.

The options we would like to include on the card are as follows:
1. Main office phone line
2. Direct phone line
3. Email address
4. Website URL
5. Name
6. Title (CEO, President, etc.)
7. Firm Address

The design and card should be double sided!!! The drop down box in the project brief for some reason is defaulting to single sided. Not sure why this is happening.

Thanks!

Contact Information for Business Card

The options we would like to include on the card are as follows: 1. Main office phone line 2. Direct phone line 3. Email address 4. Website URL 5. Name 6. Title (CEO, President, etc.) 7. Firm Address

Requirements
Must have
• Card must be double sided.

```html
<!DOCTYPE html>
<html lang="en">
<head>
<meta charset="utf-8">
<title>Ledgerline Tax Group – Business Card</title>
<link href="https://fonts.googleapis.com/css2?family=Montserrat:wght@400;500;700&display=swap" rel="stylesheet">
<style>
  :root {
    --stage: #d4d4d4;
    --card: #f3f3f3;
    --card-back-top: #ffffff;
    --card-back-bottom: #e9ebee;
    --orange: #ec7c22;
    --lime: #b9c334;
    --ink: #111111;
    --grey: #5d5d5d;
  }
  * { box-sizing: border-box; margin: 0; padding: 0; }
  html, body { width: 1200px; height: 800px; overflow: hidden; }
  body {
    background: var(--stage);
    font-family: "Montserrat", sans-serif;
    display: flex;
    align-items: center;
    justify-content: center;
    gap: 50px;
  }
  .card {
    position: relative;
    width: 540px;
    height: 310px;
    border-radius: 18px;
    overflow: hidden;
    box-shadow: 0 12px 30px rgba(0,0,0,0.15);
  }

  /* Front */
  .card-front { background: var(--card); }
  .front-band {
    position: absolute; left: 0; right: 0; bottom: 0;
    height: 46px; background: var(--orange);
  }
  .front-block {
    position: absolute; left: 50px; top: 70px;
    width: 170px; height: 194px; background: var(--orange);
  }
  .front-block-accent {
    position: absolute; left: 80px; top: 40px;
    width: 150px; height: 60px; background: var(--lime);
  }
  .front-details {
    position: absolute; left: 256px; top: 36px; right: 16px;
  }
  .person-name { font-weight: 700; font-size: 19px; color: var(--ink); letter-spacing: 0.3px; }
  .person-title { font-size: 13px; color: var(--ink); margin-top: 1px; }
  .firm-name {
    margin-top: 12px; padding-bottom: 8px;
    border-bottom: 1px solid var(--lime);
    width: 220px;
    font-weight: 500; font-size: 15px; color: var(--grey);
    letter-spacing: 0.6px; white-space: nowrap;
  }
  .contact-list { list-style: none; margin-top: 12px; }
  .contact-list li {
    display: flex; align-items: center; gap: 7px;
    font-size: 13px; color: var(--ink); line-height: 20px;
  }
  .contact-list svg { width: 11px; height: 11px; fill: var(--ink); flex: none; }
  .address { font-size: 13px; color: var(--ink); margin-top: 4px; }

  /* Back */
  .card-back {
    background: linear-gradient(160deg, var(--card-back-top) 0%, var(--card-back-bottom) 100%);
  }
  .back-brand {
    position: absolute; left: 0; right: 0; top: 78px;
    display: flex; flex-direction: column; align-items: center;
  }
  .back-square { width: 40px; height: 40px; background: var(--orange); }
  .back-name {
    margin-top: 22px; font-weight: 500; font-size: 30px;
    color: var(--grey); letter-spacing: 1px; white-space: nowrap;
  }
  .back-band {
    position: absolute; left: 0; right: 0; bottom: 22px; height: 50px;
    background: var(--lime);
    display: flex; align-items: center; justify-content: center;
    font-weight: 700; font-size: 13px; color: var(--ink);
  }
</style>
</head>
<body>

  <section class="card card-front" aria-label="Business card front">
    <div class="front-block-accent"></div>
    <div class="front-block"></div>
    <div class="front-band"></div>
    <div class="front-details">
      <p class="person-name">YOUR NAME</p>
      <p class="person-title">Title (CEO, President, etc.)</p>
      <p class="firm-name">LEDGERLINE TAX GROUP</p>
      <ul class="contact-list">
        <li><svg viewBox="0 0 24 24"><path d="M6.6 10.8a15 15 0 0 0 6.6 6.6l2.2-2.2a1 1 0 0 1 1-.25 11.4 11.4 0 0 0 3.6.57 1 1 0 0 1 1 1V20a1 1 0 0 1-1 1A17 17 0 0 1 3 4a1 1 0 0 1 1-1h3.5a1 1 0 0 1 1 1c0 1.25.2 2.45.57 3.6a1 1 0 0 1-.25 1z"/></svg>012 345 6789</li>
        <li><svg viewBox="0 0 24 24"><path d="M3 8c0-3 18-3 18 0v2h-5V8H8v2H3z"/><path d="M5 12h14l1 8H4z"/></svg>012 345 6789</li>
        <li><svg viewBox="0 0 24 24"><path d="M2 5h20v14H2z M4 7v.5l8 5 8-5V7z" fill-rule="evenodd"/></svg>yourmail@mailbox.com</li>
        <li><svg viewBox="0 0 24 24"><path d="M12 2a10 10 0 1 0 0 20 10 10 0 0 0 0-20zm0 2c.9 1.2 1.6 2.6 2 4h-4c.4-1.4 1.1-2.8 2-4zM4.3 14a8 8 0 0 1 0-4h3.5a16 16 0 0 0 0 4zm5.6 0a14 14 0 0 1 0-4h4.2a14 14 0 0 1 0 4zm6.3 0a16 16 0 0 0 0-4h3.5a8 8 0 0 1 0 4zM12 20c-.9-1.2-1.6-2.6-2-4h4c-.4 1.4-1.1 2.8-2 4z"/></svg>www.Yourwebsite.com</li>
      </ul>
      <p class="address">Your Address Here</p>
    </div>
  </section>

  <section class="card card-back" aria-label="Business card back">
    <div class="back-brand">
      <div class="back-square"></div>
      <p class="back-name">LEDGERLINE TAX GROUP</p>
    </div>
    <div class="back-band">www.Yourwebsite.com</div>
  </section>

</body>
</html>
```